Web-Design  für naturwissenschaflich-philosophische Institution
Zielgruppe
Es handelt sich um eine naturwissenschaflich-philosophische Institution. Besucher sind neben Natur- und Geisteswissenschaftlern auch interessierte Laien.
Kernthema der Seite ist alles rund um das Thema Zahlen, allerdings unter einem naturwissenschaftlich, philosophischen Aspekt. Nach einer grundsätzlichen Erklärung (Leitartikel 'Als Flüsse singen') baut die Seite sich auf aus zahreichen Beispielen/Beiträgen aus den unterschiedlichsten Fachbereichen, die scheinbar keinerlei Bezug zueinander haben, wie Mathematik, Geometrie einerseits und der großen Literatur einschließlich historischer und religiöser Schriften andererseits. Immer aber gibt es einen Bezug zu fraktal wachsenden Dreiecken.
Die Artikel sind meist populärwissenschaftlich formuliert. Es handelt sich nicht um esoterische Inhalte, auch wenn der Domainname www.kelmbrauth.de das evtl. vermuten ließe. Keine Berührung zu Spiritualität. Die Institution ist im Aufbau und hat durchaus den Anspruch, diese klassischen Themen modern aufzugreifen. Sie ist nicht verstaubt.
Aufgabenstellung
Geordneter, klarer, transparenter Aufbau. Übersichtlich und strukturiert, wie zB www.qrl.de Es sollten geometrische Proportionen eingehalten werden (wie Symmetrie, goldener Schnitt). Nicht zu viele verschiedene Stilelemente. Die Seite sollte einladend sein, ggf. ansprechendes Bild auf Startseite (mit Bezug zu Zahlen, Geoemetrie).
Die Startseite braucht nun im Header kein Logo mehr zu haben. Der Seitentitel sollte sein 'Das Echo der Wolken'. Siehe Anhang 'Header Beispiel'
Als Menüpunkte benötigen wir neben Home, nur 'Beiträge', 'Buch', 'Kontakt' oder einfach nur die bekannten drei Striche. Der Link zum Impressum genügt im Footer. Rechts oben benötigt man ein Suchfeld.
Besonderheit: Man benötigt eine Art zweiten Header, der aus einer Zahlenreihe besteht. Die einzelnen Zahlen müssen später verlinkt sein auf Unterseiten. Siehe Muster im Anhang. Der User muss sie als Link erkennen können (evtl. Programmierthema: zB Hervorheben beim drüberhoovern). Die Zahlen müssen erweiterbar sein, ggf. über Pfeil klicken, siehe
Es gibt einen zentralen Startartikel. Auf diesen muss man leicht kommen. Im Muster heißt er 'Als die Flüsse singen'.
Das Bild hier ist sehr wichtig. Es sollte bestehn aus vielen interessanten Zahlen, wie in 'Zahlenwolke' angegeben. Und möglichst auch den Dreiecken wie in 'Logo1'.
Weiter unten auf der Startseite sollte es dann weitere Elemente geben, einmal wo man zu bestimmten Unterkategorien kommt, im Muster sind das 'Bibel und Zahlen' 'Naturwissenschaft' etc. und dann evtl weiter unten noch ein Stilelemente, in welchem man die neuesten Artikel verlinken kann.

```html
<!DOCTYPE html>
<html lang="de">
<head>
<meta charset="utf-8">
<title>Das Echo der Wolken</title>
<link href="https://fonts.googleapis.com/css2?family=Poppins:wght@300;400;500;600;700&display=swap" rel="stylesheet">
<style>
:root{
  --blue:#1f8ae6;
  --blue-dark:#1565c0;
  --ink:#222831;
  --text:#5a5f66;
  --muted:#8a8f96;
  --dark-btn:#2b3440;
  --gray-band:#ececec;
  --line:#d5d7da;
  --white:#ffffff;
}
*{box-sizing:border-box;margin:0;padding:0}
html,body{width:1200px;height:5074px;overflow:hidden}
body{background:var(--white);font-family:"Poppins",sans-serif;color:var(--text);position:relative}
.page{position:absolute;left:90px;top:86px;width:1010px;height:4862px;background:var(--white);box-shadow:0 0 14px rgba(0,0,0,.18)}
.abs{position:absolute}

/* header */
.brand{left:235px;top:100px;display:flex;align-items:center;gap:8px;font-size:15px;font-weight:600;color:var(--blue)}
.brand-dot{width:22px;height:22px;border-radius:50%;background:var(--blue)}
.main-nav{left:545px;top:106px;display:flex;gap:19px;font-size:9px;font-weight:600;letter-spacing:.4px;text-transform:uppercase;color:var(--ink)}
.main-nav .active{color:var(--blue);border-bottom:2px solid var(--blue);padding-bottom:3px}
.search{left:846px;top:101px;width:106px;height:20px;border:1px solid var(--line);border-radius:3px;font-size:8px;color:#b0b3b8;padding:4px 6px;display:flex;justify-content:space-between;align-items:center}
.number-row{left:740px;top:144px;display:flex;gap:8px;font-size:11px;font-weight:500;color:var(--ink)}
.number-row .current{color:var(--blue)}
.number-row .arrow{color:var(--muted)}

/* hero */
.hero{left:90px;top:172px;width:1010px;height:434px;background:linear-gradient(135deg,#2a6fc9 0%,#3f93e6 45%,#5aa8ee 70%,#2c73cc 100%)}
.hero-title{left:238px;top:300px;font-size:44px;line-height:52px;font-weight:700;color:var(--white)}
.btn{display:inline-flex;align-items:center;justify-content:center;font-size:9px;font-weight:500;color:var(--white)}
.btn-blue{background:var(--blue)}
.btn-dark{background:var(--dark-btn)}
.hero-btn{left:238px;top:438px;width:192px;height:28px}

/* category band */
.band{left:90px;top:606px;width:1010px;height:426px;background:var(--gray-band)}
.card{top:688px;width:225px;height:266px;background:var(--white);box-shadow:0 1px 6px rgba(0,0,0,.08);padding:24px 21px}
.card h2{font-size:24px;line-height:28px;font-weight:600;color:var(--ink);margin-bottom:16px}
.card p{font-size:9px;line-height:13px;color:var(--text);height:72px}
.card .btn{width:116px;height:30px;position:absolute;left:21px;top:214px}

/* sidebar */
.sidebar{left:230px;top:1190px;width:155px;text-align:right}
.sidebar h3{font-size:13px;font-weight:500;color:var(--ink);margin:0 0 8px}
.sidebar ul{list-style:none;margin-bottom:30px}
.sidebar li{font-size:9.5px;line-height:13px;color:var(--blue);margin-bottom:6px}
.side-rule{left:406px;top:1114px;width:1px;height:646px;background:var(--line)}

/* article */
.article{left:461px;top:1114px;width:491px}
.article h1{font-size:28px;line-height:38px;font-weight:500;color:var(--ink);margin-bottom:20px}
.article p{font-size:9.5px;line-height:14px;margin-bottom:12px}
.article .lead-item{margin-bottom:12px;font-size:9.5px;line-height:14px}
.toc-title{font-weight:600;color:var(--ink)}
.toc{list-style:none;font-size:9.5px;line-height:14px;color:var(--blue)}
.toc li{margin-bottom:14px}
.toc .sub{padding-left:18px;margin-bottom:0}
.toc .subsub{padding-left:38px;margin-bottom:0}
.toc .sub:last-child,.toc .subsub.last{margin-bottom:14px}
.short-rule{left:461px;top:1892px;width:52px;height:2px;background:var(--ink)}

.figure{left:236px;top:1938px;width:152px;height:196px;background:linear-gradient(160deg,#d9d9d9,#8f8f8f 55%,#c7c7c7)}
.caption{left:236px;top:2146px;width:152px;font-size:7.5px;line-height:10px;color:var(--muted);text-align:right}

.body-col{left:461px;width:491px}
.body-col h2{font-size:12px;font-weight:600;color:var(--ink);margin-bottom:8px}
.body-col h3{font-size:11px;font-weight:600;color:var(--ink);margin-bottom:8px;padding-left:22px}
.body-col h4{font-size:9px;font-weight:600;color:var(--ink);margin-bottom:6px;padding-left:42px}
.body-col p{font-size:9.5px;line-height:14.5px;margin-bottom:12px}
.indent1 p{padding-left:42px}
.indent2 p{padding-left:63px}

.to-top{left:996px;top:4840px;width:26px;height:26px}
.footer-band{left:90px;top:4910px;width:1010px;height:38px;background:var(--gray-band)}
</style>
</head>
<body>
<div class="page"></div>

<header>
  <div class="abs brand"><span class="brand-dot"></span>Kelmbrauth.de</div>
  <nav class="abs main-nav">
    <span class="active">Home</span><span>Beiträge</span><span>Buch</span><span>Kontakt</span><span>Impressum</span>
  </nav>
  <div class="abs search">Suche
    <svg width="9" height="9" viewBox="0 0 10 10"><circle cx="4" cy="4" r="3" fill="none" stroke="#555" stroke-width="1.2"/><line x1="6.3" y1="6.3" x2="9.3" y2="9.3" stroke="#555" stroke-width="1.2"/></svg>
  </div>
  <nav class="abs number-row">
    <span class="arrow">‹</span><span class="current">1</span><span>2</span><span>3</span><span>4</span><span>5</span><span>6</span><span>7</span><span>8</span><span>9</span><span>10</span><span class="arrow">›</span>
  </nav>
</header>

<section>
  <div class="abs hero" role="img" aria-label="Blaue Zahlenwolke mit großen, überlagerten Ziffern und einem Dreieck"></div>
  <h1 class="abs hero-title">Als die Flüsse<br>singen ...</h1>
  <span class="abs btn btn-blue hero-btn">Lern mehr</span>
</section>

<section>
  <div class="abs band"></div>
  <article class="abs card" style="left:236px">
    <h2>Bibel und Zahlen</h2>
    <p>Die Heilige Schrift ist ein Werk aus Zahlen. Ihre Verfasser haben die archetypischen Inhalte in wundersamer Art und Weise in der Bibel. Und so weiter und so fort</p>
    <span class="btn btn-blue">Lern mehr</span>
  </article>
  <article class="abs card" style="left:483px">
    <h2>Naturwissens chaft</h2>
    <p>Die Heilige Schrift ist ein Werk aus Zahlen. Ihre Verfasser haben die archetypischen Inhalte in wundersamer Art</p>
    <span class="btn btn-dark">Lern mehr</span>
  </article>
  <article class="abs card" style="left:727px">
    <h2>Philosophie</h2>
    <p>Die Heilige Schrift ist ein Werk aus Zahlen. Ihre Verfasser haben die archetypischen Inhalte in wundersamer Art und Weise der Bibel. Und so weiter und so fort und vieles mehr das sehr schön eindrucksvoll ist</p>
    <span class="btn btn-dark">Lern mehr</span>
  </article>
</section>

<aside class="abs sidebar">
  <h3>Kategorien</h3>
  <ul><li>Allgemein</li></ul>
  <h3>Neue Beiträge</h3>
  <ul>
    <li>Allgemein</li><li>Das „Dazwischen“</li><li>Das Buch zum Thema</li>
    <li>Die Messschnur des Richtmaß der Welt und das Vermessen der Kreiszahl Pi</li>
    <li>Zwei Kalenderordnungen</li>
    <li>Die wahre Bedeutung der Zahlen in Wissenschaft und Religion</li>
  </ul>
  <h3>Alle Beiträge</h3>
  <ul>
    <li>Allgemein</li><li>Das „Dazwischen“</li><li>Das Buch zum Thema</li>
    <li>Die Messschnur des Richtmaß der Welt und das Vermessen der Kreiszahl Pi</li>
    <li>Zwei Kalenderordnungen</li>
    <li>Die wahre Bedeutung der Zahlen in Wissenschaft und Religion</li>
  </ul>
</aside>
<div class="abs side-rule"></div>

<article class="abs article">
  <h1>Was wirklich zählt oder als die Flüsse singen ...</h1>
  <p>Diese Frage beantwortet sich aus dem, was wir den Logos nennen und der zeigt sich uns durch ein vierfach Gegebenes:</p>
  <div class="lead-item">((1)) Sein ist Ordnung<br>Alles was ist, ist ein Ausdruck von Ordnung. Ohne Ordnung kann nichts sein.</div>
  <div class="lead-item">((2)) Ordnung ist Zahl<br>Geordnet wird stets durch die Zahl und die Ordnung an sich erscheint erst durch die Existenz von Zahlen. Ordnung und Zahl sind untrennbar miteinander verbunden. Sie sind Ausdruck ein und desselben Seins.</div>
  <div class="lead-item">((3)) Ordnung und Zahl bedeuten Beziehung<br>Da alles Ordnung und Zahl ist, besteht alles primär aus Beziehungen und nicht aus Dingen.</div>
  <div class="lead-item">((4)) Die Zahl manifestiert die ordentliche, verbindliche Beziehung zur Einheit und Ganzheit.<br>Diese Eigenschaft ist es, welche die Zahl zur Universalie macht.</div>
  <p>Die nachfolgenden Ausführungen versuchen, die vier genannten Einsichten aus den verschiedenen Perspektiven zu erhellen.</p>
  <p class="toc-title">Inhaltsverzeichnis:</p>
  <ul class="toc">
    <li>1.0 Sein und Ordnung</li>
    <li class="sub" style="padding-left:0">2.0 Ordnung ist Zahl</li>
    <li class="sub">2.1 Das Phänomen „Zahlen“</li>
    <li class="sub">2.2 Die Quantelung aller Natur</li>
    <li class="subsub">2.2.1 Raum, Zeit und Energie sind gequantelt</li>
    <li class="subsub">2.2.2 Quantensprünge der Elektronen</li>
    <li class="subsub">2.2.3 Quantelung im PSE</li>
    <li class="subsub">2.2.4 Kausalitäten sind Quanten</li>
    <li class="subsub last">2.2.5 Sinn und Bewusstsein</li>
    <li>3.0 Ordnung und Zahl bedeuten Beziehung. Alles besteht aus Beziehungen und nicht aus Dingen</li>
    <li>4.0 Die besondere Eigenschaft (Beziehung) der Zahl, welche die Zahl zur Universalie macht.</li>
    <li class="sub" style="padding-left:0">5.0 Eine Hinzufügung</li>
    <li class="sub last" style="margin-bottom:14px">5.1 ... zum Missbrauch von Zahlen</li>
    <li>6.0 Was in der „Dimension Mensch“ wirklich zählt – UNSERE AUFGABE</li>
  </ul>
</article>
<div class="abs short-rule"></div>

<div class="abs figure" role="img" aria-label="Alter Kupferstich einer sitzenden, nachdenklichen Gestalt mit Geometriewerkzeugen"></div>
<p class="abs caption">6.0 Was in der „Dimension Mensch“ wirklich zählt – UNSERE AUFGABE</p>

<section class="abs body-col" style="top:1940px">
  <h2>1.0 Sein und Ordnung</h2>
  <p style="padding-left:22px">Das Sein an sich ist abstrakt und nicht greifbar. Es kann nur durch ein So-Sein in einer Disposition (Beschaffenheit) und Anordnung in Erscheinung treten. Mit anderen Worten: Was ungeordnet ist, lässt Ordnung aufscheinen.</p>
</section>

<section class="abs body-col" style="top:2046px">
  <h2>2.0 Ordnung ist Zahl</h2>
  <p style="padding-left:22px">Ordnung ist eine definierende Abfolge von mindestens zwei Elementen. So ist die einfachste Ordnung die Verknüpfung der zwei Elemente, die zusammen ein Ganzes und Drittes darstellen. Die Vorstellung von Ordnung basiert demnach immer auf dem Zusammenwirken von drei Elementen. Die Trias bzw. deren geometrisches Symbol das Dreieck ist demnach der Urtyp von Ordnung.</p>
</section>

<section class="abs body-col indent1" style="top:2148px">
  <h3>2.1. Das Phänomen „Zahlen“</h3>
  <p style="padding-left:42px">Zählen ist ein Zuordnungsprozess. Das Erstaunliche an ihm ist, dass er direkt funktioniert. Wenn ein denkendes Geschöpf von ihnen Zahlen erfährt, kann sich dieses Geschöpf gar kein anderes Zählen vorstellen als jenes, das wir kennen. Wenn wir fragen, weshalb uns die Zahlen mit solcher Gewissheit vertraut sind, dann geben wir vielleicht davon aus, dass die Zahl und das Zählen nur Produkte des menschlichen Geistes sind. Das aber ist nicht so. Tierversuche zeigen, dass auch Tiere zählen und sogar rechnen können. Unsere Vertrautheit mit der Zahl ist vielmehr Ausdruck eines Durchdrungenseins aller Existenzen von einer Ordnung, die sich in ihrer reinsten Form in der Ordnung der Zahlen niederschlägt.</p>
  <p style="padding-left:42px">Ordnung ist per se Zahlenordnung. Erst durch die Zahl wird Ordnung sichtbar. Alles was wir als Ordnung wahrnehmen, und dazu gehören der Mikrokosmos, der Makrokosmos, sowie alles Leben, wird durch die Zahl gestaltet. Als Natur ist von der Zahl durchdrungen und ist Zahl. Das stärkste Argument dafür ist die Quantelung aller Natur. Die Quantelung besagt: Die Welt, der wir scheinbar objektiv begegnen, tritt uns immer „abgezählt“ entgegen, also in ganzen Zahlen.</p>
</section>

<section class="abs body-col" style="top:2426px">
  <h3>2.2. Die Quantelung aller Natur</h3>
</section>

<section class="abs body-col indent2" style="top:2452px;height:800px">
  <h4>2.2.1 Raum, Zeit und Energie sind gequantelt</h4>
  <p>Die physikalische Welt, wie wir sie seit der klassischen Mechanik kennen, ist eingebettet in Zeit und Raum. Sie läuft kontinuierlich ab und kennt keine Sprünge. Wir sind gewohnt, die Welt linear zu sehen. Sie gleicht dem fortlaufenden Zahlenstrahl und dem Vorstellen von einer nur unendlichen Zahl. Die lineare Vorstellung führt zur Vorstellung einer unendlichen Zahlenreihe.</p>
  <p>Solche Vorstellung verkennt die Qualität eines Ganzen und ersetzt diese durch die Vorstellung eines linearen, nichtendenden Kontinuums. Beherrscht uns das Bild der Unendlichkeit erst einmal, dann übertragen wir es naheau unbemerkt auch auf alle Teile des Ganzen. So nehmen wir an, dass sich jeder Raum zwischen zwei Zahlen ebenso wie die unendliche Zahlenreihe selbst, in unendliche Teile gliedert. Der tägliche und praktische Umgang mit gebrochenen Zahlen bestärkt diese Vorstellung: Hinter dem Komma lassen sich beliebig viele Stellen anhängen. Das täuscht eine Exaktheit und damit Sicherheit vor, die so in letzter Konsequenz nicht vorhanden sind. Die alltäglichen Beispiele von der immer genaueren Vermessung einer Küstenlinie oder der Umfangsberechnung der sogenannten Kochinseln führt uns das vor Augen. In Wirklichkeit führt uns die scheinbar zunehmende Exaktheit zu einem immer größeren Fehler. Am Ende steht sogar die völlige Unbestimmtheit.</p>
  <p>Unsere Vorstellung, die Welt wäre eine lineare, täuscht also. Vielmehr sehen wir Entwicklung und Wirklichkeit durch den Bruch. Es war nur eine Frage der Zeit, bis diese lineare Sicht auf die Welt gebrochen wurde. Der Bruch trat ein, als die Physik zur Überraschung aller Physiker nachwies, dass Energie nicht kontinuierlich, sondern in kleinen Paketen, den so genannten „Quanten“ (Wirkungsquantum) abgegeben wird. Das war die Geburtsstunde der Quantenphysik. Seit der Entdeckung des Quantenuniversums werden unsere Vorstellungen von Raum und Zeit auf vielfache Weise verletzt und wir werden mit Wirkungen konfrontiert für die man keine Ursachen mehr in Raum und Zeit angeben kann.</p>
  <p>Das Dramatische, ja regelrecht Tragische daran aber ist die Vehemenz und Unwiderruflichkeit des Erkannten. Wir wissen nämlich, dass der entdeckte Bruch wesenhaft für unsere Wirklichkeit ist und nicht mehr nur auf eine ungenügende Messgenauigkeit zurückgeführt werden kann. Brüche schaffen Wirklichkeiten.</p>
  <p>Zwischen den Zahlen befinden sich unpysische Brüche, welche die Zahlen zu dem machen, was wir von Natur aus sind, nämlich eigenständige Qualitäten im Sinne von Archetypen. Als solche sind sie wesenhaft. Sie halten allem Sein und allen Naturen an, auch Raum, Zeit und Energie. Wie die Zahlen sind sie gequantelt. Sie kommen nur in wohl definierten Portionen vor und nicht etwa in beliebigen Größen.</p>
  <p>Die durch die Quantenphysik begründete neue Physik hat Raum, Zeit und unsere bisherige lineare Vorstellung von Kausalitäten relativiert. Wir aber suchen nach letzten, nicht mehr zu hinterfragenden Entitäten. Wir suchen nach einer neuen Theorie über die Welt.</p>
  <p>Dabei ist klar: Wenn Raum, Zeit und unsere Vorstellung von Kausalität relativiert sind, bleibt</p>
</section>

<section class="abs body-col indent2" style="top:3256px;height:800px">
  <h4>2.2.2 Quantensprünge der Elektronen</h4>
  <p>Die Forschung verschaffte uns mit ihrem Atommodell einen ersten Einblick in den Mikrokosmos und seine atomaren und subatomaren Strukturen. Als Welle fuhr sich mit dem späteren Atommodell genauer beschäftigte, kam es dann im wahrsten Sinn des Wortes zu bahnbrechenden Erkenntnissen. Seit dieser Zeit haben wir Kenntnis von den sogenannten Quantensprüngen, den sprunghaften Übergängen der Elektronen von einer Energieebene auf eine andere. Wir wissen jetzt, dass die Elektronen nur auf diskreten, d.h. bestimmten, fest definierten Bahnen um den Kern kreisen. Zwischen den von uns in Bezug auf Zeit und Raum registrierten Zuständen gibt es keinerlei Zwischenzustände.</p>
  <p>Die Elektronen strahlen während ihrer stabilen Zustände keinerlei Energie ab und erleiden keinerlei Energieverlust. Nur unter dieser eigenartigen Bedingung können sie die besagten Zustände halten und „verkörpern“. Eine Energieabstrahlung erfolgt lediglich, sobald ein Elektron von einem diskreten Zustand zu einem anderen diskreten Zustand wechselt. In unserer mechanistischen Vorstellung springt es von einer äußeren auf eine inneren Bahn.</p>
  <p>Der Mikrokosmos führt uns über das lineare Atommodell und die Quantenzustände vor Augen, dass die Welt keineswegs allein durch Kontinuität zu erfassen ist, sondern dass vielmehr hinter jeder von uns wahrgenommenen Linearität jeweils deutlich voneinander getrennte, eben diskrete, Qualitäten stehen, aus denen heraus unsere Welt erst in Erscheinung tritt.</p>
  <p>Die nach dem Atommodell aufkommende Quantenphysik führte über die Quantenmechanischen Atommodelle hin zu einem „konkreten und doch wiederum so gar nicht konkreten Elementarteilchen“. Wir begegnen elementar abgegrenzten, konkreten Dingen, deren Hauptbeigenschaft ihre „Nicht-Dinglichkeit“ ist. Diese elementaren „Dinge“ in ihrer Existenz zu verstehen, das ist die große Herausforderung. Da nun jedes Ding von uns zwangsläufig in Zeit und Raum erfasst wird, und damit durch unsere festlegende Beobachtung und Bezeichnung einer Manifestation unterworfen ist, haben all die „Elementarteilchen“ eine Masse.</p>
  <p>Ausgerechnet jene so genannten Teilchen, welche von allem Teilhaftigen am ehesten die hinter allem stehende Einheit, Ganzheit und Vollkommenheit „verkörpern“ und deshalb zugleich die denkbar größte Distanz zu den Dingen und Körpern haben, konfrontieren uns erneut mit dem Bruch. Sie brechen die von der Teilchenphysik postulierte, lineare Vorstellung. Existenz beginnt erst mit der Existenz von Raum und Zeit.</p>
  <p>Hinter der Erfahrung von Masse und Geschwindigkeit verbergen sich die Größen Raum und Zeit. Die „Lichtteilchen“, welche von allem uns erscheinenden Teilhaftigen am ehesten die hinter allem stehende Einheit „verkörpern“, lösen unsere scheinbar notwendige Vorstellung von Raum und Zeit auf. Die Masse verschwindet vollständig und die Geschwindigkeit, der Ausdruck von Bewegung, nimmt einen festen, archetypischen Charakter an.</p>
  <p>Bei allem Verschwinden aber bleibt das abstrakteste aller Gebilde, die Zahl. Sie bildet sich ab in der Raum-Zeit-Formel (Raumzeit2 = Raum2 + Zeit2), einem Gleichnis des pythagoreischen Dreiecks 32 + 42 = 52, das der Theorie zugrunde liegt.</p>
</section>

<section class="abs body-col indent2" style="top:4062px;height:230px">
  <h4>2.2.3 Quantelung im Periodensystem der Elemente (PSE)</h4>
  <p>Wenn schon der subatomare Bereich von den Quanten und somit von der Zahl durchdrungen ist, dann wird diese erwartungsgemäß auch für die uns bekannte Welt der konkreten Stoffe der Fall sein. Unsere substanzielle Welt besteht in ihrem konkreten Stoff aus den chemischen Elementen. Ihr Geburtsregister ist das Periodensystem der Elemente (PSE). In ihm liegen uns die chemischen Elemente nach Zahlen geordnet vor. Die Erstellung der Ordnung war aber nur möglich, weil ihre Natur der Ordnung der ganzen Zahlen folgt. Jedes Element unterscheidet sich von seinem Nachbarn nach der Ordnungszahl, welche die Anzahl der Protonen im Atomkern wiedergibt. Die Ordnung der chemischen Elemente folgt streng der Ordnung der ganzen Zahlen. Nirgends wird die Verbindung zwischen der Zahl und der konkreten Materie offensichtlicher als im Periodensystem der Elemente.</p>
</section>

<section class="abs body-col indent2" style="top:4298px;height:510px">
  <h4>2.2.4 Kausalitäten sind Quanten</h4>
  <p>Wir nehmen Wirkzusammenhänge anhand von konkreten Erscheinungen wie Raum, Zeit und Energie u.a. wahr. Weil die Erscheinungen selbst schon, wie auch die atomaren und subatomaren Zustände gequantelt sind, müssen auch die über sie abgeleiteten Wirkzusammenhänge die Eigenschaft der Quanten einschließen. Aus solcher dinglich-linearen Sicht sind die Wirkzusammenhänge aus den Quanten und somit aus den Zahlen erwachsene Bildungsmuster.</p>
  <p>Neben der dinglich-linearen Sicht kann man die Wirkzusammenhänge auch mit der eingangs vorgestellten und von Ordnung, Zahl und Beziehung geprägten triadischen Sicht begründen. Nach ihr ist die grundlegende Ordnung eine Zahlenordnung. Sie besagt, dass primär alles aus Beziehungen und nicht aus Dingen besteht, ergo liegen die Beziehungen und somit die Wirkzusammenhänge den Dingen voraus und bilden sie und ordnen wiederum deren Beziehungen.</p>
  <p>Die dinglich-lineare und die triadische Sicht begründen das Verhältnis von Ding und Wirkung in umgekehrter Folge. Beide aber bestätigen, auf ihre Weise die Quantentheorie. Wenn die Wirklichkeit immer eine „abgezählte“ ist, dann betrifft das auch die kausalen Wirkzusammenhänge. Sie folgen aus der von uns als universell erfahrenen Quantenstruktur der Wirklichkeit nicht heraus. Ihr Wesen besteht aus Quanten.</p>
  <p>Die Quantennatur geht, wie wir wissen, mit den Zahlen einher. Dass die Zahlen eigene Entitäten und damit Qualitäten sind, lässt sich bereits aus den bisher Erörterten schließen, soll aber an anderer Stelle für die einzelnen Zahlen ausführlich gezeigt werden. Hier geht es darum, dass die Begriffe Quantum und Qualität mittels Zahl unmittelbar verknüpft sind.</p>
  <p>Die Eigenschaft eines von Anbeginn an vorhandenen Gefesselten, das seiner ersten Natur nach zugleich zusammengehört, das ist das Bild von geordneten Qualitäten im Gegensatz zur nur linear verlaufenden Quantität, wie sie uns die Vorstellung von nur zählenden Zahlen suggeriert.</p>
  <p>Kausalität und Qualität sind nicht zu trennen oder sogar ein und das gleiche. In jedem Fall aber prägen die Kausalitäten unser Denken und unsere Bewusstseinsbildung und schlagen sich nieder in »Denk- und Bildungsmustern«.</p>
</section>

<svg class="abs to-top" viewBox="0 0 26 26" role="img" aria-label="Nach oben"><polygon points="13,7 21,19 5,19" fill="#222831"/></svg>
<div class="abs footer-band"></div>
</body>
</html>
```